Design for company homepage promoting to the pharmaceutical industry

Our company produces medical education materials and services for the pharmaceutical industry. Our existing website (www.quorvane.net.au) provides more information.
 
We need a homepage design for our new company website we are creating. Our site will not have a great amount of content, we want it to be fast, user friendly and easily adaptable to viewing on any platform, and through any browser. We don't want it over-designed - i.e. no highly animated banner flags, backgrounds, obscure webfonts, too many graphics etc. Attached are files indicating our existing company logo and design. We want the logo and rings to be retained. We've also attached draft copy for the website.
The final website may be designed in Wordpress (still to be confirmed)
 
This is a design to replace the current site (www.quorvane.net.au). Content will also be revised.
Things we don't like about our current design - doesn't use our current branding, is not very exciting, old fashioned 'standard' format, too much content, just doesn't look that good, boring.
 
Examples of sites we like:
www.bralimo.com.au
http://factsheets.tenvoramed.com.au/index.html
 
Features we like from these sites - fast, responsive, short and to the point, cross-platform compatible including smartphones, and looks good
 
Main reasons people will visit our site: to find out whether we can provide services they might be looking for, to make a decision on whether they are interested in what we offer so they can get in touch with us, and to get our contact details.
Main thing we want to achieve from website visits is that it looks good enough and provides enough summary information on us so that they want to get in touch with us, to offer us work or to ask us to come in and meet them to provide more info on what we do.
Two most important calls to action from our website
· make the decision that we can do what you are looking for
· get in touch with us.
Updates

Thanks everyone for your submissions. At this stage with the Christmas break upon us, we are yet to finalise our decision, and will make a decision early in the new year. I hope everyone has a good holiday break.
Kind regards
Giles

Target Market(s)

Pharmaceutical industry professionals, marketers and medical professionals.

Industry/Entity Type

Pharmaceutical

Requirements
Must have
• Company logo and rings must be incorporated, company colour - blue - must be in there.
Should not have
• Complex animation or graphics that will slow the upload or limit cross-platform compatability/viewing on smartphones etc.

```html
<!DOCTYPE html>
<html lang="en">
<head>
<meta charset="utf-8">
<title>Quorvane Healthcare Education</title>
<link rel="stylesheet" href="https://fonts.googleapis.com/css2?family=Questrial&family=Open+Sans:wght@400;600&family=Arimo:wght@400;700&display=swap">
<style>
:root{
  --brand-blue:#0a9ad8;
  --deep-blue:#1a5a8a;
  --text-blue:#1a80c4;
  --nav-bg:#d6e9f4;
  --band-bg:#bde1f1;
  --circle-bg:#e6f1f8;
  --icon-blue:#2a6fae;
  --body-text:#555555;
  --panel-bg:#f0f4f5;
  --field-border:#e2e8ea;
  --footer-bg:#7eb0d6;
  --footer-base:#6a9fca;
  --white:#ffffff;
}
*{box-sizing:border-box;margin:0;padding:0}
html,body{width:1079px;height:1200px;overflow:hidden;background:var(--white)}
.page{position:relative;width:1079px;height:1200px;overflow:hidden;font-family:"Open Sans",sans-serif}

.site-header{position:absolute;left:0;top:0;width:100%;height:236px;border-top:1px solid #000}
.brand{position:absolute;left:0;width:100%;top:22px;text-align:center;color:var(--deep-blue);font-family:"Questrial",sans-serif}
.brand-name{font-size:64px;line-height:1;letter-spacing:1px}
.brand-name::after{content:"";display:inline-block;width:9px;height:9px;border-radius:50%;background:#8ab8de;margin-left:6px;vertical-align:top}
.brand-tag{font-size:10px;letter-spacing:1.5px;margin-top:4px}

.main-nav{position:absolute;left:0;top:236px;width:100%;height:46px;background:var(--nav-bg);display:flex}
.main-nav a{display:block;height:46px;line-height:46px;text-decoration:none;color:var(--deep-blue);font-size:15.5px;text-align:center}
.main-nav a.is-active{background:var(--brand-blue);color:var(--white);width:116px}

.services{position:absolute;left:0;top:282px;width:100%;height:241px;background:var(--band-bg)}
.service{position:absolute;top:28px;width:185px}
.service-icon{width:84px;height:84px;border-radius:50%;background:var(--circle-bg);margin:0 auto;display:flex;align-items:center;justify-content:center}
.service-icon span{display:block;width:44px;height:40px;border-radius:6px;background:var(--icon-blue)}
.service h2{font-family:"Questrial",sans-serif;font-weight:400;font-size:20px;color:var(--deep-blue);text-align:center;margin-top:14px;letter-spacing:.3px}
.service p{font-size:12.6px;line-height:13.5px;color:var(--text-blue);margin-top:4px}

.intro{position:absolute;left:23px;top:546px;width:620px}
.intro h1{font-family:"Questrial",sans-serif;font-weight:400;font-size:23.5px;line-height:26px;color:var(--brand-blue);width:560px}
.intro p{font-size:15.2px;line-height:19.5px;color:var(--body-text);margin-top:10px}
.intro ul{list-style:none;margin-top:14px}
.intro li{position:relative;padding-left:42px;font-size:15.2px;line-height:18.5px;color:var(--body-text);margin-bottom:12px}
.intro li::before{content:"";position:absolute;left:12px;top:5px;width:10px;height:10px;border-radius:50%;background:#666}

.contact-panel{position:absolute;left:723px;top:545px;width:343px;height:354px;background:var(--panel-bg)}
.contact-panel h2{position:absolute;left:24px;top:18px;font-family:"Questrial",sans-serif;font-weight:400;font-size:19px;color:var(--brand-blue)}
.field{position:absolute;left:21px;width:301px;height:35px;background:var(--white);border:1px solid var(--field-border);font-family:"Arimo",sans-serif;font-size:13px;color:#8aa5c0;padding:9px 10px}
.field-message{height:111px}
.submit-btn{position:absolute;left:24px;top:307px;width:118px;height:32px;background:var(--brand-blue);color:var(--white);font-family:"Arimo",sans-serif;font-size:13.5px;text-align:center;line-height:32px}

.site-footer{position:absolute;left:0;top:945px;width:100%;height:225px;background:var(--footer-bg);color:var(--white);font-family:"Arimo",sans-serif}
.site-footer h3{position:absolute;top:37px;font-family:"Questrial",sans-serif;font-weight:400;font-size:19px;letter-spacing:.3px}
.footer-links{position:absolute;top:73px;list-style:none;font-size:13px;line-height:17.6px}
.testimonial-icon{position:absolute;left:366px;top:73px;width:50px;height:50px}
.quote{position:absolute;left:429px;width:300px;font-size:13px;line-height:15.6px}
.social{position:absolute;left:814px;top:75px;display:flex;gap:8px}
.social span{width:31px;height:31px;border-radius:50%;background:#e8f1f8}
.newsletter-note{position:absolute;left:815px;top:120px;font-size:11.5px;line-height:14px}
.email-field{position:absolute;left:812px;top:159px;width:204px;height:29px;border-radius:15px;background:var(--white);color:var(--deep-blue);font-size:11.5px;line-height:29px;padding-left:17px}
.subscribe{position:absolute;left:816px;top:203px;font-size:11.5px;font-weight:700}
.copyright{position:absolute;left:0;top:1170px;width:100%;height:30px;background:var(--footer-base);color:var(--white);font-family:"Arimo",sans-serif;font-size:12px;line-height:30px;padding-left:20px}
</style>
</head>
<body>
<div class="page">
  <header class="site-header">
    <div class="brand">
      <div class="brand-name">quorvane</div>
      <div class="brand-tag">HEALTHCARE EDUCATION</div>
    </div>
  </header>

  <nav class="main-nav">
    <a class="is-active" href="#">Home</a>
    <a href="#" style="width:158px">Who We Are</a>
    <a href="#" style="width:122px">What We Do</a>
    <a href="#" style="width:118px">Clients</a>
    <a href="#" style="width:84px">Work</a>
    <a href="#" style="width:166px">Testimonials</a>
    <a href="#" style="width:144px">Contact Us</a>
    <a href="#" style="width:110px">Login</a>
  </nav>

  <section class="services">
    <div class="service" style="left:16px">
      <div class="service-icon" role="img" aria-label="Laptop icon"><span></span></div>
      <h2>PROMOTION</h2>
      <p>Quorvane can help you promote your brand – from the development of strategic communication campaigns .</p>
    </div>
    <div class="service" style="left:237px">
      <div class="service-icon" role="img" aria-label="Microscope icon"><span></span></div>
      <h2>EDUCATION</h2>
      <p>Clinical papers, evidence summaries, scientific newsletters and accredited educational materials.</p>
    </div>
    <div class="service" style="left:451px">
      <div class="service-icon" role="img" aria-label="Programs icon"><span></span></div>
      <h2>PROGRAMS</h2>
      <p>From clinical audits to patient support activities, Quorvane has successfully develop and complex program.</p>
    </div>
    <div class="service" style="left:667px">
      <div class="service-icon" role="img" aria-label="Group of people icon"><span></span></div>
      <h2>MEETINGS</h2>
      <p>You will maximise your investment in scientific meetings by employing Quorvane to manage the entire process.</p>
    </div>
    <div class="service" style="left:883px">
      <div class="service-icon" role="img" aria-label="Laboratory flask icon"><span></span></div>
      <h2>IME</h2>
      <p>In an environment of ever-increasing scrutiny over the support that pharmaceutical companies.</p>
    </div>
  </section>

  <section class="intro">
    <h1>At Quorvane we are healthcare communication specialists; this means we’re scientists, journalists and marketers rolled into one.</h1>
    <p>As you can see we provide all the things you’d expect from a top-class healthcare communications agency, but we have the depth of technical understanding and creative flair to produce sophisticated and memorable materials and programs, including:</p>
    <ul>
      <li>Strategic tools for brand promotion (such as detail aids, product monographs, slide kits and patient materials)</li>
      <li>Non-promotional materials for market education (e.g. clinical papers and evidence summaries)</li>
      <li>Complex programs such as clinical audits and product familiarisation programs</li>
      <li>Medical meetings and symposia</li>
    </ul>
  </section>

  <aside class="contact-panel">
    <h2>CONTACT US</h2>
    <div class="field" style="top:52px">Full Name</div>
    <div class="field" style="top:96px">Email</div>
    <div class="field" style="top:140px">Telephone</div>
    <div class="field field-message" style="top:184px">Message</div>
    <div class="submit-btn">Submit</div>
  </aside>

  <footer class="site-footer">
    <h3 style="left:17px">NAVIGATION</h3>
    <ul class="footer-links" style="left:19px">
      <li>Home</li><li>Who We Are</li><li>What We Do</li><li>Clients</li><li>Work</li><li>Testimonials</li>
    </ul>
    <ul class="footer-links" style="left:129px">
      <li>Contact Us</li><li>Login</li><li>Privacy Policy</li><li>Terms of Use</li>
    </ul>

    <h3 style="left:363px">TESTIMONIAL</h3>
    <svg class="testimonial-icon" viewBox="0 0 50 50" role="img" aria-label="Speech bubble icon">
      <circle cx="20" cy="20" r="17" fill="none" stroke="#fff" stroke-width="2.5"/>
      <circle cx="34" cy="32" r="13" fill="#fff"/>
    </svg>
    <p class="quote" style="top:74px">“Congratulations &amp; many thanks for your seriously wonderful &amp; successful work on the weekend. I'm especially grateful for the calm, cool &amp; very clever work done in managing all the planning process before I even came on board – truly outstanding”</p>
    <p class="quote" style="left:363px;width:370px;top:164px">“Thank you for all your help with making the meeting the huge success that it was”</p>

    <h3 style="left:817px">CONNECT WITH US</h3>
    <div class="social" aria-label="Social links"><span></span><span></span><span></span><span></span><span></span></div>
    <p class="newsletter-note">subscribe to our monthly newsletter<br>and get the best deals and discounts</p>
    <div class="email-field">enter email address</div>
    <div class="subscribe">➤&nbsp;&nbsp;subscribe now</div>
  </footer>
  <div class="copyright">© Copyright 2013 Quorvane. All Rights Reserved</div>
</div>
</body>
</html>
```